Brisket Dwelling Review is a leading provider of residential appraisal and home inspection products in S

I need a business card/logo designed that obviously describes my business. We are a residential appraisal and home inspection company in Springfield, MO. We offer residential appraisals, home inspection, pest inspection and radon gas measurement. We have been in business for 18 years and hold state certified residential appraisal licenses and VORMEL certified home inspection licenses. I have a logo that I really like and will attach, but would be open to new suggestions. I like more modern designs than traditional and would like a two sided card with our services, licenses and qualifications on the back.

```html
<!DOCTYPE html>
<html lang="en">
<head>
<meta charset="utf-8">
<title>Brisket Dwelling Review – Business Card</title>
<link href="https://fonts.googleapis.com/css2?family=Roboto:wght@400;500;700&display=swap" rel="stylesheet">
<style>
  :root {
    --bg: #1c1c1e;
    --card: #ffffff;
    --orange: #f39a21;
    --brand-brown: #8a6a45;
    --ink-grey: #4d5560;
    --rule-grey: #e3e3e3;
    --white: #ffffff;
    --divider: rgba(255,255,255,0.55);
  }
  * { margin: 0; padding: 0; box-sizing: border-box; }
  html, body { width: 1200px; height: 800px; overflow: hidden; }
  body {
    background: var(--bg);
    font-family: "Roboto", Arial, sans-serif;
    position: relative;
  }
  .card {
    position: absolute;
    width: 560px;
    height: 320px;
    background: var(--card);
    box-shadow: 0 10px 30px rgba(0,0,0,0.45);
    overflow: hidden;
  }
  /* Front */
  .card-front { left: 130px; top: 60px; }
  .brand {
    position: absolute;
    left: 46px;
    top: 122px;
    display: flex;
    align-items: center;
    gap: 14px;
  }
  .brand-mark {
    width: 26px; height: 26px;
    background: var(--orange);
    flex: none;
  }
  .brand-name {
    font-size: 32px;
    font-weight: 700;
    color: var(--brand-brown);
    line-height: 1.05;
    letter-spacing: 0.3px;
  }
  .tabs {
    position: absolute;
    right: 0; top: 0;
    width: 118px; height: 100%;
    display: flex;
    flex-direction: column;
    gap: 4px;
  }
  .tab {
    flex: 1;
    background: var(--orange);
    border-radius: 10px 0 0 10px;
  }
  .tab:nth-child(2) { margin-left: 10px; }
  .tab:nth-child(3) { margin-left: 20px; }
  /* Back */
  .card-back { left: 510px; top: 420px; }
  .person {
    position: absolute;
    left: 46px;
    top: 128px;
  }
  .person-name {
    font-size: 22px;
    font-weight: 500;
    color: var(--orange);
    letter-spacing: 0.5px;
  }
  .person-role {
    font-size: 13px;
    color: var(--ink-grey);
    margin-top: 2px;
    letter-spacing: 0.4px;
  }
  .contact-panel {
    position: absolute;
    right: 28px;
    top: 36px;
    width: 262px;
    height: 172px;
    background: var(--orange);
    padding: 12px 18px;
    display: flex;
    flex-direction: column;
    justify-content: space-around;
  }
  .contact-row {
    display: flex;
    align-items: center;
    gap: 12px;
    padding-bottom: 8px;
    border-bottom: 1px solid var(--divider);
    color: var(--white);
    font-size: 12.5px;
  }
  .contact-icon {
    width: 24px; height: 24px;
    border: 1.5px solid var(--white);
    border-radius: 5px;
    display: flex; align-items: center; justify-content: center;
    flex: none;
  }
  .contact-icon svg { width: 14px; height: 14px; }
  .credentials {
    position: absolute;
    left: 46px;
    right: 28px;
    top: 228px;
    border-top: 1px solid var(--rule-grey);
    padding-top: 12px;
    display: flex;
    flex-direction: column;
    gap: 7px;
  }
  .credential-line {
    display: flex;
    gap: 10px;
    font-size: 11px;
    color: var(--ink-grey);
    line-height: 1.35;
  }
  .credential-label {
    flex: none;
    width: 92px;
    font-weight: 500;
    color: var(--orange);
    text-transform: uppercase;
    letter-spacing: 0.6px;
    font-size: 10px;
    padding-top: 1px;
  }
</style>
</head>
<body>

  <section class="card card-front">
    <div class="brand">
      <span class="brand-mark"></span>
      <span class="brand-name">Brisket Dwelling<br>Review</span>
    </div>
    <div class="tabs">
      <div class="tab"></div>
      <div class="tab"></div>
      <div class="tab"></div>
    </div>
  </section>

  <section class="card card-back">
    <div class="person">
      <p class="person-name">DANA WHITLOW</p>
      <p class="person-role">Executive Director</p>
    </div>
    <div class="contact-panel">
      <div class="contact-row">
        <span class="contact-icon">
          <svg viewBox="0 0 24 24"><path fill="#fff" d="M6.6 10.8a15.1 15.1 0 0 0 6.6 6.6l2.2-2.2a1 1 0 0 1 1-.25 11.4 11.4 0 0 0 3.6.57 1 1 0 0 1 1 1V20a1 1 0 0 1-1 1A17 17 0 0 1 3 4a1 1 0 0 1 1-1h3.5a1 1 0 0 1 1 1c0 1.25.2 2.45.57 3.57a1 1 0 0 1-.25 1z"/></svg>
        </span>
        <span>+123 555 0147</span>
      </div>
      <div class="contact-row">
        <span class="contact-icon">
          <svg viewBox="0 0 24 24"><circle cx="12" cy="12" r="9" fill="none" stroke="#fff" stroke-width="2"/><path d="M3 12h18M12 3c3 3.2 3 14.8 0 18M12 3c-3 3.2-3 14.8 0 18" fill="none" stroke="#fff" stroke-width="1.6"/></svg>
        </span>
        <span>www.brisketdwelling.com</span>
      </div>
      <div class="contact-row">
        <span class="contact-icon">
          <svg viewBox="0 0 24 24"><rect x="3" y="6" width="18" height="12" rx="1" fill="#fff"/><path d="M3.5 6.5 12 13l8.5-6.5" fill="none" stroke="#f39a21" stroke-width="1.6"/></svg>
        </span>
        <span>dana@brisketdwelling.com</span>
      </div>
    </div>
    <div class="credentials">
      <p class="credential-line">
        <span class="credential-label">Services</span>
        <span>Residential Appraisals · Home Inspection · Pest Inspection · Radon Gas Measurement</span>
      </p>
      <p class="credential-line">
        <span class="credential-label">Licenses</span>
        <span>State Certified Residential Appraiser · VORMEL Certified Home Inspector · 18 Years in Business</span>
      </p>
    </div>
  </section>

</body>
</html>
```